Lantern & Row Theatre Academy Business Card

We need a professional looking card for the Lantern & Row Theatre Academy. The logo is attached.
The owner is: Maribel Quistorp
Phone Number: 303-555-0147
Email: lrtheatreacademy@mailbox-demo.com
Website: lrtheatre-demo.com
Somewhere on the front of the card we would like to see the slogan: Step into the limelight
On the back we would like to see the quote: All the world's a stage. -Edmund Pelgrave
We are open to different colors for the wording or maybe just black. Something that will go well with the logo.
Target Market(s)
Individuals seeking a professional children's theatre.
Industry/Entity Type
Business
Colors
Look and feel

```html
<!DOCTYPE html>
<html lang="en">
<head>
<meta charset="utf-8">
<title>Lantern &amp; Row Theatre Academy – Business Card</title>
<link rel="stylesheet" href="https://fonts.googleapis.com/css2?family=Crimson+Text:ital,wght@0,400;0,600;1,400&family=Alegreya+Sans:wght@400&display=swap">
<style>
  :root {
    --page-bg: #e9e7e6;
    --card-white: #ffffff;
    --blush-light: #fbeff2;
    --blush: #f1c9d3;
    --blush-deep: #e7a9b9;
    --curtain: #8e1230;
    --curtain-dark: #5d0a1f;
    --floor-light: #7a4530;
    --floor-dark: #4a2516;
    --brand-red: #b5152b;
    --brand-faint: #efc6cd;
    --ink: #1d1a1b;
  }
  * { box-sizing: border-box; margin: 0; padding: 0; }
  html, body { width: 1200px; height: 900px; overflow: hidden; }
  body {
    background: var(--page-bg);
    display: flex;
    align-items: center;
    justify-content: center;
    gap: 40px;
  }
  .card {
    position: relative;
    width: 540px;
    height: 309px;
    overflow: hidden;
    border-radius: 3px;
    box-shadow: 0 10px 30px rgba(0,0,0,.18);
  }

  /* Front */
  .card-front {
    background: linear-gradient(135deg, var(--blush-light) 0%, var(--blush) 65%, var(--blush-deep) 100%);
    font-family: "Crimson Text", Georgia, serif;
  }
  .stage-curtain {
    position: absolute;
    left: 0; top: 0;
    width: 100%; height: 48px;
    background: linear-gradient(180deg, var(--curtain) 0%, var(--curtain-dark) 70%, rgba(93,10,31,.35) 100%);
  }
  .stage-floor {
    position: absolute;
    left: 0; top: 48px; bottom: 0;
    width: 128px;
    background: linear-gradient(180deg, var(--floor-light) 0%, var(--floor-dark) 100%);
  }
  .stage-spotlight {
    position: absolute;
    right: 0; bottom: 0;
    width: 240px; height: 200px;
    background: radial-gradient(closest-side at 60% 55%, rgba(255,255,255,.95) 0%, rgba(244,219,225,.6) 45%, rgba(241,201,211,0) 100%);
  }
  .front-content {
    position: absolute;
    left: 158px; top: 70px;
  }
  .brand {
    display: flex;
    align-items: center;
    gap: 10px;
    margin-bottom: 12px;
  }
  .brand-name {
    font-size: 26px;
    font-weight: 600;
    color: var(--brand-red);
    line-height: 1.05;
  }
  .brand-mark {
    width: 30px; height: 30px;
    background: var(--brand-red);
  }
  .owner-name {
    font-size: 17px;
    color: var(--ink);
    margin-bottom: 6px;
  }
  .contact-list { list-style: none; }
  .contact-item {
    display: flex;
    align-items: center;
    gap: 8px;
    font-size: 14px;
    color: var(--ink);
    line-height: 1.45;
  }
  .contact-icon { width: 12px; height: 12px; flex: none; }
  .slogan {
    position: absolute;
    left: 158px; bottom: 22px;
    font-size: 16px;
    font-style: italic;
    color: var(--brand-red);
  }

  /* Back */
  .card-back {
    background: var(--card-white);
    font-family: "Alegreya Sans", Tahoma, sans-serif;
  }
  .back-brand {
    position: absolute;
    left: 200px; top: 62px;
    display: flex;
    align-items: center;
    gap: 10px;
  }
  .back-brand-name {
    font-family: "Crimson Text", Georgia, serif;
    font-size: 24px;
    font-weight: 600;
    color: var(--brand-faint);
    line-height: 1.05;
  }
  .back-brand-mark {
    width: 28px; height: 28px;
    background: var(--brand-faint);
  }
  .quote {
    position: absolute;
    left: 30px; top: 112px;
    font-size: 48px;
    color: var(--ink);
    white-space: nowrap;
  }
  .quote-author {
    position: absolute;
    right: 40px; top: 178px;
    font-family: "Crimson Text", Georgia, serif;
    font-size: 16px;
    color: var(--ink);
  }
</style>
</head>
<body>

  <section class="card card-front" aria-label="Business card front">
    <div class="stage-curtain" role="img" aria-label="Red velvet stage curtain tied back"></div>
    <div class="stage-floor" role="img" aria-label="Wooden stage floor boards"></div>
    <div class="stage-spotlight" role="img" aria-label="Stage spotlight on a stand casting soft light"></div>

    <div class="front-content">
      <div class="brand">
        <span class="brand-name">Lantern &amp; Row<br>Theatre Academy</span>
        <span class="brand-mark" aria-hidden="true"></span>
      </div>
      <p class="owner-name">Maribel Quistorp</p>
      <ul class="contact-list">
        <li class="contact-item">
          <svg class="contact-icon" viewBox="0 0 12 12" aria-hidden="true"><rect width="12" height="12" rx="2" fill="#1d1a1b"/><path d="M3.5 2.8c.4-.3.8-.2 1 .2l.6 1.2c.1.3 0 .6-.2.8l-.4.3c.4.9 1 1.5 1.9 1.9l.3-.4c.2-.2.5-.3.8-.2l1.2.6c.4.2.5.6.2 1-.5.8-1.2 1-2 .7C5 8.4 3.6 7 3 5.2c-.3-.8-.1-1.7.5-2.4z" fill="#fff"/></svg>
          303-555-0147
        </li>
        <li class="contact-item">
          <svg class="contact-icon" viewBox="0 0 12 12" aria-hidden="true"><rect width="12" height="12" rx="2" fill="#1d1a1b"/><rect x="2.5" y="3.5" width="7" height="5" fill="none" stroke="#fff" stroke-width="1"/><path d="M2.5 3.5 6 6.3 9.5 3.5" fill="none" stroke="#fff" stroke-width="1"/></svg>
          lrtheatreacademy@mailbox-demo.com
        </li>
        <li class="contact-item">
          <svg class="contact-icon" viewBox="0 0 12 12" aria-hidden="true"><circle cx="6" cy="6" r="6" fill="#1d1a1b"/><circle cx="6" cy="6" r="4" fill="none" stroke="#fff" stroke-width=".8"/><ellipse cx="6" cy="6" rx="1.8" ry="4" fill="none" stroke="#fff" stroke-width=".8"/><path d="M2 6h8" stroke="#fff" stroke-width=".8"/></svg>
          lrtheatre-demo.com
        </li>
      </ul>
    </div>
    <p class="slogan">Step into the limelight</p>
  </section>

  <section class="card card-back" aria-label="Business card back">
    <div class="back-brand">
      <span class="back-brand-name">Lantern &amp; Row<br>Theatre Academy</span>
      <span class="back-brand-mark" aria-hidden="true"></span>
    </div>
    <p class="quote">All the world's a stage</p>
    <p class="quote-author">Edmund Pelgrave</p>
  </section>

</body>
</html>
```